Web Design Project

We need a design for the actual web.
http://mirela.vunto.example/
It will be a cakes and cupcakes online shop.

It is a one page site, with five anchors.

Inicio (Home)
Here it will show a brief explanation about our shop, just explaining we sell really nice cakes and cupcakes. Also we want to show a slide gallery, like the one it is working, but with not nice choosen pictures.

Productos/Tortas
This two anchors will be just one at the end, but I wanted to show the two options for accessing the different products, tabs or buttons. You can click on the firsts images on that links for see the "pop up image" with a better explanation of every product.

Contacto
Here it will show a little form, that will only appear in smartphones and maybe tablets, this form needs to be similar and much more simple than the principal form (the next anchor), so just focus on it once the next one its done.

Form
This will be the way the users will send the orders, its a complex form, focused on the UX. We dont want the user to type too much and we want it to surprise the user and fell really comfortable.

Industry/Entity Type

Tv

Requirements
Must have

• -Must have side menu, but you can redesign it completelly, but with the same structure
-Its important to focus all the content in the top and middle, we arent sure about users screens and it we set info at the footer, maybe its not gonna show (no scroll vertical).
-You can change all the colours of the site, we are open to new visions, you can surprise us.

```html
<!DOCTYPE html>
<html lang="es">
<head>
<meta charset="utf-8">
<title>Lila Bakes — Handmade Bakery</title>
<link rel="stylesheet" href="https://fonts.googleapis.com/css2?family=Dancing+Script:wght@600;700&family=PT+Sans:wght@400;700&display=swap">
<style>
:root{
  --rose:#e7737a;
  --rose-deep:#d95f68;
  --glow:#f3bb94;
  --cream:#fdf9ee;
  --card:#f4eddc;
  --peach-top:#f6c59a;
  --peach-bottom:#f0a577;
  --brown:#6b4540;
  --ink:#6d5a52;
  --muted:#a58d74;
  --pink-text:#e76d74;
  --nav-text:#fdf0df;
  --lime:#e4ef5a;
}
*{margin:0;padding:0;box-sizing:border-box}
html,body{width:841px;height:1200px;overflow:hidden}
body{
  position:relative;
  background:radial-gradient(ellipse 420px 330px at 420px 220px,var(--glow) 0%,#eea083 45%,var(--rose) 100%);
  font-family:"PT Sans",Tahoma,sans-serif;
  color:var(--ink);
}
.nav{position:absolute;left:0;width:841px;display:flex;justify-content:center;align-items:center;gap:12px;list-style:none}
.nav a{font-family:"Dancing Script",cursive;font-weight:700;font-size:17px;color:var(--nav-text);text-decoration:none;text-shadow:0 1px 1px rgba(120,40,40,.35)}
.nav a.current{color:#c98a7c}
.nav .dot{width:5px;height:5px;border-radius:50%;background:var(--rose-deep)}
.nav-top{top:28px}
.nav-bottom{top:1108px}
.rule{position:absolute;left:170px;width:500px;height:1px;background:linear-gradient(90deg,transparent,rgba(255,240,225,.8),transparent)}
.rule::after{content:"";position:absolute;left:244px;top:-3px;width:12px;height:7px;border-radius:50%;border:1px solid rgba(255,240,225,.9)}
.brand{position:absolute;top:78px;left:0;width:841px;display:flex;justify-content:center;align-items:center;gap:10px}
.brand-mark{width:50px;height:50px;border-radius:50%;background:#8a5a48}
.brand-text{display:flex;flex-direction:column}
.brand-name{font-family:"PT Sans",sans-serif;font-weight:700;font-size:30px;line-height:1;color:var(--lime)}
.brand-tag{font-family:"Dancing Script",cursive;font-size:12px;color:var(--brown);letter-spacing:1px;margin-top:4px}
.frame{position:absolute;left:94px;top:206px}
.slider{position:absolute;left:128px;top:240px}
.arrow{position:absolute;top:394px;width:40px;height:46px;border-radius:50%;background:#f3a59c;display:flex;align-items:center;justify-content:center;box-shadow:0 1px 3px rgba(0,0,0,.15)}
.arrow-prev{left:104px}.arrow-next{left:697px}
.welcome{position:absolute;left:128px;top:512px;width:587px;height:126px;border-radius:0 0 8px 8px;background:linear-gradient(var(--peach-top),var(--peach-bottom));text-align:center;padding-top:10px}
.welcome h1{font-family:"Dancing Script",cursive;font-weight:700;font-size:30px;color:#d94c5c;line-height:1.1}
.welcome p{font-size:11px;line-height:14px;color:#fff6ea;margin:8px 54px 0}
.cards{position:absolute;top:653px;left:128px;display:flex;gap:13px}
.card{width:187px;height:209px;background:var(--card);text-align:center}
.card-photo{height:67px}
.card h2{font-family:"Dancing Script",cursive;font-weight:700;font-size:17px;color:var(--brown);margin-top:12px}
.card h2 span{color:var(--pink-text)}
.card p{font-size:8px;line-height:12.5px;color:var(--muted);margin:10px 22px 0}
.card p b{font-weight:400;color:var(--ink)}
.btn{display:inline-block;margin-top:12px;width:63px;height:20px;line-height:20px;background:var(--brown);color:#f7eadb;font-size:8px;font-weight:700;letter-spacing:.3px}
.links{position:absolute;left:128px;top:930px;list-style:none}
.links li{display:flex;align-items:center;gap:6px;height:16.2px;font-size:6.5px;color:#fde8de;text-transform:uppercase}
.links li::before{content:"";width:9px;height:8px;border-radius:4px 4px 1px 1px;background:linear-gradient(#fff 0 45%,#8a5a48 45%)}
.divider{position:absolute;left:295px;top:928px;width:1px;height:130px;background:rgba(255,230,220,.45)}
.feature-photo{position:absolute;left:328px;top:928px;width:137px;height:117px;background:#fff;padding:8px;box-shadow:0 1px 4px rgba(0,0,0,.15)}
.feature-photo div{width:100%;height:100%}
.feature-text{position:absolute;left:478px;top:938px;width:240px}
.feature-text h3{font-family:"Dancing Script",cursive;font-weight:700;font-size:17px;color:#fff6ea}
.feature-text p{font-size:7.5px;line-height:12.4px;color:#fde6dc;margin-top:8px}
.feature-text .more{display:block;text-align:right;font-size:7.5px;font-weight:700;color:#fde6dc;margin-top:10px}
.copyright{position:absolute;top:1172px;left:0;width:841px;text-align:center;font-size:7.5px;font-weight:700;color:#fde8de;letter-spacing:.2px}
.copyright i{display:inline-block;width:5px;height:5px;border-radius:50%;background:var(--rose-deep);margin:0 6px;vertical-align:middle}
.top-btn{position:absolute;left:780px;top:1111px;width:27px;height:27px;border-radius:50%;background:var(--rose-deep);color:#fde8de;font-size:6.5px;display:flex;align-items:center;justify-content:center}
</style>
</head>
<body>
<ul class="nav nav-top">
  <li><a class="current" href="#inicio">Inicio</a></li><li class="dot"></li>
  <li><a href="#productos">Productos</a></li><li class="dot"></li>
  <li><a href="#tortas">Tortas</a></li><li class="dot"></li>
  <li><a href="#contacto">Contacto</a></li><li class="dot"></li>
  <li><a href="#form">Form</a></li>
</ul>
<div class="rule" style="top:57px"></div>

<div class="brand">
  <div class="brand-mark"></div>
  <div class="brand-text">
    <span class="brand-name">Lila Bakes</span>
    <span class="brand-tag">Handmade Bakery</span>
  </div>
</div>

<svg class="frame" width="655" height="686" viewBox="0 0 655 686">
  <path d="M0 90 Q0 70 30 58 Q327 -30 625 58 Q655 70 655 90 V686 H0 Z" fill="var(--cream)"/>
</svg>

<svg class="slider" width="587" height="272" viewBox="0 0 587 272" role="img" aria-label="Photo of cupcakes with yellow frosting and berries, with a shop tag">
  <defs>
    <linearGradient id="slide" x1="0" y1="0" x2="0" y2="1">
      <stop offset="0" stop-color="#e8a24c"/>
      <stop offset=".55" stop-color="#f2d48a"/>
      <stop offset="1" stop-color="#8c7864"/>
    </linearGradient>
  </defs>
  <path d="M0 60 Q0 40 30 32 Q293 -25 557 32 Q587 40 587 60 V272 H0 Z" fill="url(#slide)"/>
</svg>
<div class="arrow arrow-prev"><svg width="10" height="14"><path d="M8 1 L2 7 L8 13" stroke="#fff" stroke-width="2.5" fill="none"/></svg></div>
<div class="arrow arrow-next"><svg width="10" height="14"><path d="M2 1 L8 7 L2 13" stroke="#fff" stroke-width="2.5" fill="none"/></svg></div>

<section class="welcome" id="inicio">
  <h1>Welcome to Lila Bakes!</h1>
  <p>Finalmente ya esta disponible en Santiago de Chile nuestro catalogo de sabrosos Cupcakes y Tortas Con ingredientes 100% naturales y elaborados artesanalmente No solo hay que tener en cuenta la presentacion fabulosa de los mismos, lo que mas destacan nuestros clientes es el sabor exquisito y la textura.</p>
</section>

<div class="cards">
  <article class="card">
    <div class="card-photo" role="img" aria-label="Photo of a chocolate cake with shavings" style="background:linear-gradient(135deg,#c98b4a,#5a2e1e)"></div>
    <h2><span>Delicious</span> Cakes</h2>
    <p><b>Lorem ipsum dolor sit amet.</b> Vivamus tempor lacinia nisi, nec pellentesque velit mattis sit amet. Phasellus eu ipsum enim, quis interdum augue.</p>
    <a class="btn">MORE</a>
  </article>
  <article class="card">
    <div class="card-photo" role="img" aria-label="Photo of cupcakes topped with raspberries" style="background:linear-gradient(135deg,#3a1a14,#b23a3a)"></div>
    <h2><span>Best</span> Quality</h2>
    <p><b>Lorem ipsum dolor sit amet.</b> Vivamus tempor lacinia nisi, nec pellentesque velit mattis sit amet. Phasellus eu ipsum enim, quis interdum augue.</p>
    <a class="btn">MORE</a>
  </article>
  <article class="card">
    <div class="card-photo" role="img" aria-label="Photo of a cream cake with red berries" style="background:linear-gradient(135deg,#7a8a3a,#efe6d6)"></div>
    <h2><span>See Our</span> Selection</h2>
    <p><b>Lorem ipsum dolor sit amet.</b> Vivamus tempor lacinia nisi, nec pellentesque velit mattis sit amet. Phasellus eu ipsum enim, quis interdum augue.</p>
    <a class="btn">MORE</a>
  </article>
</div>

<ul class="links">
  <li>Check out cake 1!</li><li>Check out cake 2!</li><li>Check out cake 3!</li><li>Check out cake 4!</li>
  <li>Check out cake 5!</li><li>Check out cake 6!</li><li>Check out cake 7!</li><li>Check out cake 8!</li>
</ul>
<div class="divider"></div>
<div class="feature-photo"><div role="img" aria-label="Photo of a white cake decorated with strawberries" style="background:radial-gradient(circle at 55% 45%,#fbf3ea 0 30%,#d94a4a 36%,#6a4a2a 60%,#2a1a10)"></div></div>
<div class="feature-text">
  <h3>Lorem ipsum dolor sit amet.</h3>
  <p>Lorem ipsum dolor sit amet, consectetur adipiscing elit. Vivamus tempor lacinia nisi, nec pellentesque velit mattis sit amet. Phasellus eu ipsum enim, quis interdum augue. Nullam lacus lorem, ornare in ullamcorper vitae, cursus eget risus.</p>
  <span class="more">MORE</span>
</div>

<div class="rule" style="top:1088px"></div>
<ul class="nav nav-bottom">
  <li><a class="current" href="#inicio">Inicio</a></li><li class="dot"></li>
  <li><a href="#productos">Productos</a></li><li class="dot"></li>
  <li><a href="#tortas">Tortas</a></li><li class="dot"></li>
  <li><a href="#contacto">Contacto</a></li><li class="dot"></li>
  <li><a href="#form">Form</a></li>
</ul>
<div class="rule" style="top:1152px"></div>
<p class="copyright">LILA BAKES © 2012<i></i>PRIVACY POLICY</p>
<div class="top-btn">TOP</div>
</body>
</html>
```